Simple, bright, clean website - 3 pages, easy to update with WordPress!

I want to update my website (brelvatix.com) with a brighter/cleaner interface. It is quite dark right now. I would like it to be similar to a partner site (https://www.nodavent-44.com/). White with some orange highlights (matching the logo). I want to be able to easily update the site content. There should be 3 main pages: About, Services, Contact. I also like a design similar to quorfen.com

Target Market(s)

Anyone using technology to achieve business goals.

Industry/Entity Type

Managed Service Provider (IT)

Coding

Coded - Design and coding required

Number of Pages Required

3 page

Colors
F0912C
F2A743
F7CA91
FBE8D2
FDF5EE

Requirements
Must have
• Links to standard social media apps like WorkLattice, Pallgrove, etc.. Easy to edit and add pages.

```html
<!DOCTYPE html>
<html lang="en">
<head>
<meta charset="utf-8">
<title>Brelvatix – IT Solutions</title>
<link href="https://fonts.googleapis.com/css2?family=Poppins:wght@300;400;500;600;700&family=Roboto:wght@400;500;700&display=swap" rel="stylesheet">
<style>
:root{
  --orange:#F0912C;
  --orange-2:#F2A743;
  --orange-3:#F7CA91;
  --orange-4:#FBE8D2;
  --orange-5:#FDF5EE;
  --ink:#1f1f1f;
  --text:#555;
  --muted:#777;
  --dark-btn:#4a4a4a;
  --white:#fff;
}
*{box-sizing:border-box;margin:0;padding:0}
html,body{width:1200px;height:3750px;overflow:hidden}
body{position:relative;background:var(--white);font-family:'Poppins',sans-serif;color:var(--ink)}
.abs{position:absolute}
a{color:inherit;text-decoration:none}

/* header */
.top-bar{left:0;top:0;width:1200px;height:6px;background:var(--orange-2)}
.wordmark{display:flex;align-items:center;gap:10px;font-family:'Poppins',sans-serif;font-weight:500;color:var(--ink);line-height:1}
.wordmark .mark{width:16px;height:16px;background:var(--orange-2)}
.site-logo{left:82px;top:46px;font-size:34px}
.utility{right:76px;top:20px;display:flex;gap:18px;font-size:11px;color:#333;align-items:center}
.utility span{display:flex;align-items:center;gap:5px}
.main-nav{left:717px;top:64px;display:flex;gap:29px;font-size:12.5px;color:#222;text-transform:uppercase}
.btn-orange{background:var(--orange-2);color:#222;font-weight:600;font-size:11.5px;border-radius:6px;display:flex;align-items:center;justify-content:center;box-shadow:0 3px 0 var(--orange)}
.header-cta{left:983px;top:55px;width:141px;height:32px}

/* hero */
.hero{left:0;top:106px;width:1200px;height:578px;background:linear-gradient(100deg,#d9d9d9 0%,#bdbdbd 35%,#c9c2b8 60%,#e8e4de 100%)}
.hero-title{left:83px;top:284px;font-size:51px;font-weight:300;color:#111;white-space:nowrap}
.hero-sub{left:80px;top:349px;width:262px;height:38px;background:rgba(40,40,40,.75);color:#fff;font-size:26px;font-weight:300;padding-left:4px;line-height:38px;white-space:nowrap}
.hero-cta{left:80px;top:403px;width:157px;height:41px}

/* about */
.about-img-a{left:151px;top:773px;width:402px;height:533px;border-radius:40px 0 40px 40px;background:linear-gradient(160deg,#e3ddd4,#b9aa96 60%,#8a7a66)}
.about-img-b{left:381px;top:875px;width:281px;height:373px;border-radius:30px 30px 0 0;background:linear-gradient(170deg,#1f3342,#2c5166 50%,#6b4f3a)}
.tag{left:716px;top:792px;background:var(--orange-2);color:#222;font-size:8.5px;font-weight:700;border-radius:9px;padding:4px 9px;text-transform:uppercase}
.about-title{left:716px;top:824px;font-size:28px;font-weight:600;line-height:34px;color:#222;white-space:nowrap}
.about-copy{left:722px;top:905px;width:390px;font-size:10.3px;line-height:17px;color:#555;font-weight:300}
.about-copy p+p{margin-top:18px}
.since{left:718px;top:1070px;width:140px;text-align:center}
.since .year{font-size:66px;font-weight:600;color:var(--orange-2);line-height:1}
.since .label{display:flex;align-items:center;gap:8px;justify-content:center;font-size:12px;font-weight:600;margin-top:6px}
.since .label::before,.since .label::after{content:"";width:38px;height:2px;background:#444}
.checks{left:884px;top:1070px;list-style:none;font-size:12.5px;color:#444}
.checks li{display:flex;align-items:center;gap:8px;height:30px}
.tick{width:15px;height:15px;flex:0 0 15px}
.btn-dark{left:718px;top:1223px;width:134px;height:37px;border-radius:5px;background:var(--dark-btn);color:#fff;font-size:13px;font-weight:600;display:flex;align-items:center;justify-content:center}
.watch{left:875px;top:1214px;display:flex;align-items:center;gap:12px;font-size:12.5px;font-weight:600}
.play{width:52px;height:52px;border-radius:50%;background:#fff;box-shadow:0 3px 10px rgba(0,0,0,.18);display:flex;align-items:center;justify-content:center}

/* services */
.services-band{left:0;top:1395px;width:1200px;height:405px;background:linear-gradient(90deg,#c98a22,#e3a33a 40%,#d4962d 70%,#c88920)}
.services-title{left:0;top:1448px;width:1200px;text-align:center;font-size:50px;font-weight:700;color:#fff;letter-spacing:2px}
.services-sub{left:0;top:1520px;width:1200px;text-align:center;font-size:13.5px;color:#fff;line-height:20px;letter-spacing:.3px;font-weight:300}
.card{top:1597px;width:223px;height:303px;background:#fff;box-shadow:0 4px 10px rgba(0,0,0,.15);border-radius:0 0 4px 4px}
.card .thumb{height:159px;background:linear-gradient(160deg,#e0e0e0,#7a7a7a 60%,#2f2f2f)}
.card h3{margin:26px 0 0 19px;font-size:11.5px;font-weight:600;display:flex;align-items:center;gap:12px}
.card h3::after{content:"";flex:0 0 42px;height:1px;background:var(--orange-2);margin-left:auto;margin-right:19px}
.card p{margin:14px 19px 0;font-size:9.3px;line-height:16.5px;color:#444}
.arrow{top:1717px;width:34px;height:34px;border-radius:50%;background:#fff;box-shadow:0 2px 6px rgba(0,0,0,.25);display:flex;align-items:center;justify-content:center}

/* features */
.eyebrow{font-family:'Roboto',sans-serif;font-size:12px;font-weight:500;color:#222;display:flex;align-items:center;gap:12px}
.eyebrow::after{content:"";width:100px;height:1px;background:var(--orange-2)}
.feature-title{font-family:'Roboto',sans-serif;font-size:26px;font-weight:500;line-height:30px;color:#111}
.feature-copy{font-family:'Roboto',sans-serif;font-size:10.5px;line-height:19.5px;color:#666;width:405px}
.feature-copy p+p{margin-top:19px}
.why-img{left:614px;top:1983px;width:509px;height:383px;background:linear-gradient(150deg,#c9d3de,#556b86 45%,#2b3f5f 80%)}
.cyber-img{left:74px;top:2391px;width:508px;height:383px;background:linear-gradient(135deg,#1b3556,#2f6da3 50%,#0f1e33)}
.ring{width:52px;height:52px}

/* contact */
.contact-bg{left:0;top:2858px;width:1200px;height:523px;background:linear-gradient(90deg,#f1f1f1,#e4e4e4 60%,#cfcfcf)}
.contact-title{left:0;top:2885px;width:1200px;text-align:center;font-family:'Roboto',sans-serif;font-size:44px;font-weight:700;letter-spacing:1px;color:#111}
.form-panel{left:128px;top:2963px;width:945px;height:376px;background:rgba(244,244,244,.92)}
.field-label{font-size:10px;color:#333}
.field{height:36px;border:1px solid #bbb;border-radius:5px;background:#fff}
.submit{left:512px;top:3286px;width:156px;height:40px;border-radius:5px;background:var(--orange-2);color:#fff;font-weight:600;font-size:13.5px;display:flex;align-items:center;justify-content:center;letter-spacing:.5px}

/* newsletter */
.newsletter{left:0;top:3381px;width:1200px;height:147px;background:var(--orange-2)}
.news-title{left:0;top:3402px;width:1200px;text-align:center;font-size:20px;font-weight:400;color:#111}
.news-title b{font-weight:700}
.news-sub{left:0;top:3432px;width:1200px;text-align:center;font-size:12.5px;color:#222}
.news-input{left:296px;top:3464px;width:467px;height:41px;background:var(--orange-5);font-size:10px;color:#999;padding-left:10px;line-height:41px}
.news-btn{left:763px;top:3464px;width:141px;height:41px;background:#111;color:#fff;font-size:10.5px;font-weight:600;display:flex;align-items:center;justify-content:center}

/* footer */
.footer{left:0;top:3528px;width:1200px;height:222px;background:#f3f3f3}
.footer-logo{left:76px;top:3604px;font-size:32px}
.foot-col h4{font-size:13px;font-weight:600;color:var(--orange-2);margin-bottom:6px}
.foot-col li{list-style:none;font-size:13px;color:#222;height:26px;display:flex;align-items:center;gap:7px}
.foot-col .caret{color:var(--orange-2)}
.socials{display:flex;gap:8px}
.social{width:36px;height:36px;border-radius:50%;border:2px solid var(--orange)}
.foot-rule{left:74px;top:3691px;width:1052px;height:1px;background:#777}
.copyright{left:76px;top:3706px;font-size:8.5px;color:#333}
.legal{left:761px;top:3706px;font-size:8.5px;color:#333;display:flex;gap:8px}
</style>
</head>
<body>

<div class="abs top-bar"></div>

<header>
  <div class="abs wordmark site-logo"><span>Brelvatix</span><span class="mark"></span></div>
  <div class="abs utility">
    <span><svg width="12" height="12" viewBox="0 0 24 24"><path fill="#222" d="M6.6 10.8a15 15 0 0 0 6.6 6.6l2.2-2.2c.3-.3.7-.4 1-.2 1.1.4 2.3.6 3.6.6.6 0 1 .4 1 1V20c0 .6-.4 1-1 1A17 17 0 0 1 3 4c0-.6.4-1 1-1h3.5c.6 0 1 .4 1 1 0 1.3.2 2.5.6 3.6.1.3 0 .7-.2 1z"/></svg>(905) 555-0182</span>
    <span><svg width="12" height="12" viewBox="0 0 24 24"><circle cx="12" cy="7" r="5" fill="#222"/><path fill="#222" d="M2 23c0-6 4.5-9 10-9s10 3 10 9z"/></svg>CLIENT LOGIN</span>
  </div>
  <nav class="abs main-nav"><a>About Us</a><a>Services</a><a>Contact Us</a></nav>
  <a class="abs btn-orange header-cta">CONNECT MY TECH</a>
</header>

<section>
  <div class="abs hero" role="img" aria-label="Smiling support agent wearing a headset in a bright office with colleagues at computers"></div>
  <h1 class="abs hero-title">Elevate your tech journey</h1>
  <div class="abs hero-sub">with our IT solutions</div>
  <a class="abs btn-orange hero-cta">CONNECT MY TECH</a>
</section>

<section>
  <div class="abs about-img-a" role="img" aria-label="Business team meeting around a table with laptops"></div>
  <div class="abs about-img-b" role="img" aria-label="Technician working on network equipment in a server room"></div>
  <div class="abs tag">Welcome to our company</div>
  <h2 class="abs about-title">One Of The Fastest Way<br>To Gain Business Success</h2>
  <div class="abs about-copy">
    <p>There are many variations of passages of Lorem Ipsum available, but the majority have suffered alteration in some form, by injected humour, or randomised words which don't look even slightly believable.</p>
    <p>If you are going to use a passage of Lorem Ipsum, you need to be sure there isn't anything embarrassing hidden in the middle of text. All the Lorem Ipsum generators on the Internet tend to repeat predefined chunks as necessary, making this the first true generator on the Internet.</p>
  </div>
  <div class="abs since"><div class="year">1995</div><div class="label">SINCE</div></div>
  <ul class="abs checks">
    <li><svg class="tick" viewBox="0 0 16 16"><circle cx="8" cy="8" r="8" fill="#555"/><path d="M4.5 8.2l2.3 2.2 4.5-4.6" stroke="#fff" stroke-width="1.8" fill="none"/></svg>Managed IT Services</li>
    <li><svg class="tick" viewBox="0 0 16 16"><circle cx="8" cy="8" r="8" fill="#555"/><path d="M4.5 8.2l2.3 2.2 4.5-4.6" stroke="#fff" stroke-width="1.8" fill="none"/></svg>IT Consulting</li>
    <li><svg class="tick" viewBox="0 0 16 16"><circle cx="8" cy="8" r="8" fill="#555"/><path d="M4.5 8.2l2.3 2.2 4.5-4.6" stroke="#fff" stroke-width="1.8" fill="none"/></svg>VoIP Solutions</li>
    <li><svg class="tick" viewBox="0 0 16 16"><circle cx="8" cy="8" r="8" fill="#555"/><path d="M4.5 8.2l2.3 2.2 4.5-4.6" stroke="#fff" stroke-width="1.8" fill="none"/></svg>Cloud Services</li>
  </ul>
  <a class="abs btn-dark">Read More</a>
  <div class="abs watch"><div class="play"><svg width="40" height="40" viewBox="0 0 40 40"><circle cx="20" cy="20" r="19" fill="var(--orange-2)"/><path d="M16 12l12 8-12 8z" fill="#fff"/></svg></div>Watch Video</div>
</section>

<section>
  <div class="abs services-band" role="img" aria-label="Orange-toned photo of IT staff working at computer monitors"></div>
  <h2 class="abs services-title">OUR SERVICES</h2>
  <p class="abs services-sub">Many desktop publishing packages and web page editors now use Lorem Ipsum as their default model text,<br>and a search for 'lorem ipsum' will uncover many web sites still in their infancy.</p>

  <article class="abs card" style="left:141px"><div class="thumb" role="img" aria-label="Hands typing on a keyboard with network icons"></div><h3>Managed IT Services</h3><p>Many desktop publishing packages and web page editors now use Lorem Ipsum as their default model text.</p></article>
  <article class="abs card" style="left:381px"><div class="thumb" role="img" aria-label="Consultants reviewing work at a computer"></div><h3>IT Consulting</h3><p>Many desktop publishing packages and web page editors now use Lorem Ipsum as their default model text.</p></article>
  <article class="abs card" style="left:622px"><div class="thumb" role="img" aria-label="Headset beside a laptop with VoIP graphics"></div><h3>VoIP Solutions</h3><p>Many desktop publishing packages and web page editors now use Lorem Ipsum as their default model text.</p></article>
  <article class="abs card" style="left:860px"><div class="thumb" role="img" aria-label="Cloud computing graphic over a city"></div><h3>Cloud Services</h3><p>Many desktop publishing packages and web page editors now use Lorem Ipsum as their default model text.</p></article>

  <div class="abs arrow" style="left:99px"><svg width="14" height="14" viewBox="0 0 14 14"><path d="M9 2L4 7l5 5" stroke="#222" stroke-width="2.4" fill="none"/></svg></div>
  <div class="abs arrow" style="left:1090px"><svg width="14" height="14" viewBox="0 0 14 14"><path d="M5 2l5 5-5 5" stroke="#222" stroke-width="2.4" fill="none"/></svg></div>
</section>

<section>
  <div class="abs eyebrow" style="left:109px;top:2020px">Why Choose us</div>
  <h2 class="abs feature-title" style="left:109px;top:2056px">Future proof your<br>business with our IT solutions</h2>
  <div class="abs feature-copy" style="left:109px;top:2131px">
    <p>everywhere and caters to businesses that want to enhance workplace culture by employing inclusive strategies. Training and consultation services offer business leaders and employees alike a wealth of training experience, disability expertise, and firsthand knowledge.</p>
    <p>Training and consultation are individual and customized for all businesses, regardless of size to ensure inclusion of individuals with disabilities in all aspects of life.</p>
  </div>
  <div class="abs why-img" role="img" aria-label="Colleagues gathered around a laptop in a meeting"></div>
  <svg class="abs ring" style="left:588px;top:2018px" viewBox="0 0 52 52"><circle cx="26" cy="28" r="22" fill="#fff" stroke="var(--orange-2)" stroke-width="2.5"/><line x1="26" y1="2" x2="26" y2="22" stroke="var(--orange-2)" stroke-width="2.5"/></svg>
</section>

<section>
  <div class="abs cyber-img" role="img" aria-label="Person typing on a laptop with a shield lock and web address overlay"></div>
  <svg class="abs ring" style="left:554px;top:2432px" viewBox="0 0 52 52"><circle cx="26" cy="28" r="22" fill="#fff" stroke="var(--orange-2)" stroke-width="2.5"/><line x1="26" y1="2" x2="26" y2="22" stroke="var(--orange-2)" stroke-width="2.5"/></svg>
  <div class="abs eyebrow" style="left:620px;top:2486px">Our Additional Services</div>
  <h2 class="abs feature-title" style="left:620px;top:2514px">Cybersecurity Solutions</h2>
  <div class="abs feature-copy" style="left:620px;top:2572px;width:410px">
    <p>everywhere and caters to businesses that want to enhance workplace culture by employing inclusive strategies. Training and consultation services offer business leaders and employees alike a wealth of training experience, disability expertise, and firsthand knowledge.</p>
    <p>Training and consultation are individual and customized for all businesses, regardless of size to ensure inclusion of individuals with disabilities in all aspects of life. Talking about disability inclusion doesn't have to be overwhelming.</p>
  </div>
</section>

<section>
  <div class="abs contact-bg" role="img" aria-label="Faded greyscale photo of an office team"></div>
  <h2 class="abs contact-title">LET’S GET IN TOUCH</h2>
  <div class="abs form-panel"></div>
  <label class="abs field-label" style="left:249px;top:3003px">Full Name</label>
  <div class="abs field" style="left:249px;top:3026px;width:341px"></div>
  <label class="abs field-label" style="left:610px;top:3003px">Company Name</label>
  <div class="abs field" style="left:610px;top:3026px;width:341px"></div>
  <label class="abs field-label" style="left:249px;top:3074px">Your Email</label>
  <div class="abs field" style="left:249px;top:3097px;width:341px"></div>
  <label class="abs field-label" style="left:610px;top:3074px">How can we help you?</label>
  <div class="abs field" style="left:610px;top:3097px;width:341px"></div>
  <label class="abs field-label" style="left:249px;top:3143px">Your Email</label>
  <div class="abs field" style="left:249px;top:3165px;width:709px;height:104px"></div>
  <a class="abs submit">SUBMIT</a>
</section>

<section>
  <div class="abs newsletter"></div>
  <h2 class="abs news-title">SUBSCRIBE TO OUR <b>NEWSLETTER</b></h2>
  <p class="abs news-sub">Sign up with your email address to receive our regular tricks &amp; tips newsletter.</p>
  <div class="abs news-input">Enter your email</div>
  <a class="abs news-btn">SUBSCRIBE NOW</a>
</section>

<footer>
  <div class="abs footer"></div>
  <div class="abs wordmark footer-logo"><span>Brelvatix</span><span class="mark"></span></div>
  <div class="abs foot-col" style="left:412px;top:3583px">
    <h4>QUICK LINK</h4>
    <ul><li><span class="caret">›</span>HOME</li><li><span class="caret">›</span>SERVICE</li><li><span class="caret">›</span>CONTACT</li></ul>
  </div>
  <div class="abs foot-col" style="left:620px;top:3583px">
    <h4>CONTACT</h4>
    <ul>
      <li><svg width="14" height="11" viewBox="0 0 14 11"><rect width="14" height="11" rx="1" fill="var(--orange-2)"/><path d="M1 1l6 5 6-5" stroke="#fff" fill="none"/></svg>INFO@BRELVATIX.COM</li>
      <li><svg width="14" height="14" viewBox="0 0 24 24"><rect width="24" height="24" rx="3" fill="var(--orange-2)"/><path fill="#fff" d="M7.5 10.8a11 11 0 0 0 5.7 5.7l1.9-1.9c.2-.2.5-.3.8-.2.9.3 1.9.5 2.9.5v3.1H17A12 12 0 0 1 5 6V4.9h3.1c0 1 .2 2 .5 2.9z"/></svg>403-555-0147</li>
    </ul>
  </div>
  <div class="abs foot-col" style="left:890px;top:3583px">
    <h4>FOLLOW WITH US</h4>
    <div class="socials">
      <a class="social" aria-label="Pallgrove"></a>
      <a class="social" aria-label="Shutterloop"></a>
      <a class="social" aria-label="Chirpline"></a>
    </div>
  </div>
  <div class="abs foot-rule"></div>
  <p class="abs copyright">©BRELVATIX.COM</p>
  <p class="abs legal"><span>PRIVACY POLICY</span><span>|</span><span>TERMS OF SERVICE</span><span>|</span><span>COOKIE SETTINGS</span></p>
</footer>

</body>
</html>
```